TealFathom.com Website design needed!!

We are looking for a website layout to match the attached logo. We specialize in Dive Charters and currently are located in the Virgin Islands off of St. Thomas. Please create a design that is compatible with Bootstrap and have the grid in mind. WE are looking for creative and extremely professional layout design.

Target Market(s)

Scuba Diving, Divers looking for a diving charter in the Virgin Islands.

Number of Pages Required

3 page

Font styles to use
Serif

Requirements
Must have
• Must be Bootstrap friendly.
• Must work with the logo we provided. Colors etc.

```html
<!DOCTYPE html>
<html lang="en">
<head>
<meta charset="utf-8">
<title>Teal Fathom – Dive Charters St. Thomas</title>
<link rel="stylesheet" href="https://fonts.googleapis.com/css2?family=Roboto:wght@400;500;700&display=swap">
<style>
:root{
  --red:#d8262b;
  --red-dark:#b81d22;
  --nav-blue:#1f9fdc;
  --deep-blue:#0b4f8f;
  --ocean:#1a74b8;
  --panel-blue:#2e93cf;
  --ink:#1d1d1d;
  --body:#666;
  --grey-bg:#f1f1f1;
  --dark:#111;
  --white:#fff;
}
*{box-sizing:border-box;margin:0;padding:0}
html,body{width:1200px;height:2308px;overflow:hidden}
body{font-family:"Roboto",Arial,sans-serif;color:var(--ink);background:var(--white);position:relative}
.abs{position:absolute}
.photo{position:absolute}

/* top ocean backdrop */
.ocean-backdrop{left:0;top:0;width:1200px;height:700px;
  background:linear-gradient(180deg,#0d63a8 0%,#1479c0 45%,#2b8fd0 80%,#ffffff 100%)}

/* header */
.site-header{left:89px;top:0;width:1022px;height:123px;background:var(--white)}
.brand{left:34px;top:40px;display:flex;align-items:center;gap:10px}
.brand-dot{width:30px;height:30px;border-radius:50%;background:var(--red)}
.brand-name{font-size:26px;font-weight:700;color:var(--red)}
.brand-sub{left:74px;top:76px;font-size:10px;font-weight:500;color:var(--deep-blue);letter-spacing:1px}
.call{left:582px;top:52px;display:flex;align-items:center;gap:10px;font-size:20px;color:var(--ink)}
.call svg{display:block}
.socials{left:866px;top:48px;display:flex;gap:8px}
.socials span{width:28px;height:28px;border-radius:50%;background:var(--deep-blue);border:2px solid #dfe6ee}

/* nav */
.main-nav{left:89px;top:123px;width:1022px;height:62px;background:var(--nav-blue);display:flex}
.main-nav a{display:flex;align-items:center;justify-content:center;color:var(--white);text-decoration:none;font-size:16px;height:62px}
.main-nav a.active{background:#1a1a1a;width:137px}

/* hero */
.hero{left:89px;top:185px;width:1022px;height:515px;
  background:linear-gradient(135deg,#0e6c8c 0%,#1a8aa8 35%,#0b5b8e 70%,#0a3f74 100%)}
.hero-title{right:24px;top:327px;font-size:50px;font-weight:500;color:var(--white)}
.hero-sub{right:30px;top:392px;font-size:26px;font-weight:500;color:var(--white)}
.hero-arrows{right:38px;top:445px;display:flex;gap:6px}
.hero-arrows span{width:34px;height:34px;border-radius:50%;background:#1c2a36;display:flex;align-items:center;justify-content:center}

/* welcome */
.welcome-title{left:0;width:1200px;top:743px;text-align:center;font-size:24px;font-weight:500}
.accent{color:var(--red)}
.welcome-text{left:100px;width:1000px;top:786px;text-align:center;font-size:12px;line-height:21px;color:var(--body)}

/* services */
.services{left:0;top:885px;width:1200px;height:341px;background:var(--grey-bg)}
.section-title{font-size:20px;font-weight:500;color:var(--ink)}
.services .section-title{left:89px;top:33px}
.services .pager{left:1080px;top:32px}
.card{top:76px;width:245px}
.card .photo{left:0;top:0;width:245px;height:154px;border:3px solid var(--white)}
.card-title{position:absolute;top:173px;left:0;font-size:13px;font-weight:500;color:var(--ink)}
.card-text{position:absolute;top:196px;left:0;width:245px;font-size:11px;line-height:20px;color:#888}

/* charters */
.charters-photo{left:89px;top:1269px;width:429px;height:269px;border:4px solid var(--white);box-shadow:0 0 0 1px #ddd;
  background:linear-gradient(160deg,#0d5fa6 0%,#1c86c9 50%,#0a4686 100%)}
.charters-title{left:541px;top:1275px;font-size:20px;font-weight:500}
.charters-text{left:541px;top:1310px;width:570px;font-size:12px;line-height:21px;color:var(--body)}
.charters-text p+p{margin-top:21px}
.btn-red{left:543px;top:1495px;width:138px;height:35px;background:linear-gradient(180deg,#e5393d,var(--red-dark));border-radius:3px;color:var(--white);font-size:12px;font-weight:700;display:flex;align-items:center;justify-content:center}

/* news */
.news{left:0;top:1600px;width:1200px;height:412px;background:var(--grey-bg)}
.news .section-title{left:89px;top:40px}
.news-item{left:89px;width:650px;height:132px}
.news-item .photo{left:0;top:0;width:185px;height:132px}
.news-head{position:absolute;left:200px;top:0;font-size:14px;font-weight:500}
.news-date{position:absolute;left:200px;top:30px;font-size:12px;color:var(--red)}
.news-text{position:absolute;left:200px;top:52px;width:450px;font-size:11px;line-height:21px;color:#555}

.search-panel{left:764px;top:30px;width:345px;height:350px;background:var(--panel-blue);border:4px solid var(--white);box-shadow:0 0 0 1px #ddd}
.search-title{position:absolute;left:0;width:337px;top:22px;text-align:center;font-size:15px;line-height:22px;font-weight:500;color:var(--white)}
.radio{position:absolute;left:26px;font-size:11px;color:var(--white);display:flex;align-items:center;gap:8px}
.radio i{width:8px;height:8px;border-radius:50%;background:var(--white);display:block}
.field{position:absolute;left:26px;width:286px;height:48px;background:var(--white);font-size:12px;color:#555;padding:0 14px;display:flex;align-items:center}
.btn-find{position:absolute;left:26px;top:262px;width:286px;height:50px;background:linear-gradient(180deg,#e5393d,var(--red-dark));border-radius:3px;color:var(--white);font-size:14px;font-weight:500;display:flex;align-items:center;justify-content:center}

/* footer */
.site-footer{left:0;top:2012px;width:1200px;height:221px;background:linear-gradient(180deg,#1570b4,#0d5a99)}
.foot-title{position:absolute;top:40px;font-size:15px;font-weight:500;color:var(--white)}
.foot-links{position:absolute;left:89px;top:72px;list-style:none;font-size:11px;line-height:24.5px;color:var(--white)}
.foot-links li::before{content:"▸ ";font-size:9px}
.foot-text{position:absolute;font-size:11px;line-height:18px;color:var(--white)}
.newsletter-form{position:absolute;left:905px;top:116px;display:flex}
.newsletter-form .email{width:148px;height:30px;background:var(--white);font-size:11px;color:#555;display:flex;align-items:center;padding-left:12px}
.newsletter-form .submit{width:55px;height:30px;background:var(--red);color:var(--white);font-size:11px;display:flex;align-items:center;justify-content:center}
.foot-icons{position:absolute;left:905px;top:164px;display:flex;gap:17px}
.foot-icons span{width:32px;height:32px;border-radius:50%;border:1px solid rgba(255,255,255,.8)}
.copyright{left:0;top:2233px;width:1200px;height:75px;background:var(--dark);color:var(--white);font-size:11px;display:flex;align-items:center;justify-content:center}
</style>
</head>
<body>

<div class="abs ocean-backdrop" role="img" aria-label="Underwater blue ocean backdrop"></div>

<header class="abs site-header">
  <div class="abs brand"><span class="brand-dot"></span><span class="brand-name">Teal Fathom</span></div>
  <div class="abs brand-sub">ST. THOMAS</div>
  <div class="abs call">
    <svg width="16" height="16" viewBox="0 0 16 16"><rect width="16" height="16" rx="2" fill="#d8262b"/><path d="M5 3.5l1.6 2.2-1 1c.6 1.3 1.5 2.2 2.8 2.8l1-1 2.2 1.6-.9 1.6C7.5 11.6 4.4 8.5 4.3 4.4z" fill="#fff"/></svg>
    <span>CALL US: (844)-555-0192</span>
  </div>
  <div class="abs socials"><span></span><span></span><span></span><span></span></div>
</header>

<nav class="abs main-nav">
  <a class="active" href="#">HOME</a>
  <a href="#" style="width:176px">TEAL FATHOM</a>
  <a href="#" style="width:180px">ABOUT US</a>
  <a href="#" style="width:160px">CONTACT</a>
  <a href="#" style="width:200px">LEARN MORE</a>
  <a href="#" style="width:169px">SCHEDULE</a>
</nav>

<section class="abs hero" role="img" aria-label="Photo of two scuba divers posing underwater above a coral reef">
  <div class="abs hero-title">TEAL FATHOM</div>
  <div class="abs hero-sub">Neque porro quisquam est qui</div>
  <div class="abs hero-arrows">
    <span><svg width="12" height="14" viewBox="0 0 12 14"><path d="M8 2L3 7l5 5" stroke="#fff" stroke-width="2" fill="none"/></svg></span>
    <span><svg width="12" height="14" viewBox="0 0 12 14"><path d="M4 2l5 5-5 5" stroke="#fff" stroke-width="2" fill="none"/></svg></span>
  </div>
</section>

<h1 class="abs welcome-title">WELCOME TO <span class="accent">TEAL FATHOM</span></h1>
<p class="abs welcome-text">Lorem Ipsum has been the industry's standard dummy text ever since the 1500s, when an unknown printer took a galley of type and scrambled it to make a type specimen book. It has survived not only five centuries, but also the leap into electronic typesetting, remaining essentially unchanged. It was popularised in the 1960s with the release of Typeset sheets containing Lorem Ipsum passages, and more recently with desktop publishing software like Folio Layout including versions of Lorem Ipsum.</p>

<section class="abs services">
  <h2 class="abs section-title">OUR <span class="accent">SERVICE</span></h2>
  <svg class="abs pager" width="32" height="20" viewBox="0 0 32 20"><path d="M10 3L3 10l7 7M22 3l7 7-7 7" stroke="#222" stroke-width="2" fill="none"/></svg>
  <div class="abs card" style="left:89px">
    <div class="photo" role="img" aria-label="Photo of a diver giving the OK sign underwater" style="background:linear-gradient(150deg,#0b4f8f,#1b7cc4)"></div>
    <div class="card-title">NEQUE PORRO QUISQUAM</div>
    <div class="card-text">Lorem Ipsum has been the industry's standard dummy text ever since the 1500s,</div>
  </div>
  <div class="abs card" style="left:346px">
    <div class="photo" role="img" aria-label="Photo of two divers with masks close together" style="background:linear-gradient(150deg,#14609f,#2a8ccc)"></div>
    <div class="card-title">NEQUE PORRO QUISQUAM</div>
    <div class="card-text">Lorem Ipsum has been the industry's standard dummy text ever since the 1500s,</div>
  </div>
  <div class="abs card" style="left:603px">
    <div class="photo" role="img" aria-label="Photo of two divers swimming over a reef" style="background:linear-gradient(160deg,#1c8bb5,#2f9c9a)"></div>
    <div class="card-title">NEQUE PORRO QUISQUAM</div>
    <div class="card-text">Lorem Ipsum has been the industry's standard dummy text ever since the 1500s,</div>
  </div>
  <div class="abs card" style="left:860px">
    <div class="photo" role="img" aria-label="Photo of a diver above a sandy seabed" style="background:linear-gradient(170deg,#1e7fc0,#3aa3a8 80%,#6aa66e)"></div>
    <div class="card-title">NEQUE PORRO QUISQUAM</div>
    <div class="card-text">Lorem Ipsum has been the industry's standard dummy text ever since the 1500s,</div>
  </div>
</section>

<div class="abs charters-photo" role="img" aria-label="Photo of a diver with mask and regulator among bubbles"></div>
<h2 class="abs charters-title">TEAL FATHOM <span class="accent">CHARTERS AND SCUBA</span></h2>
<div class="abs charters-text">
  <p>Lorem Ipsum has been the industry's standard dummy text ever since the 1500s, when an unknown printer took a galley of type and scrambled it to make a type specimen book. It has survived not only five centuries, but also the leap into electronic typesetting, remaining essentially unchanged. It was popularised in the 1960s with the release of Typeset sheets containing</p>
  <p>It has survived not only five centuries, but also the leap into electronic typesetting, remaining essentially unchanged. It was popularised in the 1960s with the release of Typeset sheets containing Lorem Ipsum passages, and more recently with desktop publishing software</p>
</div>
<div class="abs btn-red">FREE ESSENTIAL</div>

<section class="abs news">
  <h2 class="abs section-title">LATEST <span class="accent">NEWS</span></h2>
  <article class="abs news-item" style="top:86px">
    <div class="photo" role="img" aria-label="Photo of a diver standing on a beach holding fins" style="background:linear-gradient(180deg,#8fc3e0,#4aa6c8 55%,#d8cfb8)"></div>
    <div class="news-head">Nemo Enim Ipsam Volup</div>
    <div class="news-date">09-07-2015</div>
    <p class="news-text">Lorem Ipsum has been the industry's standard dummy text ever since the 1500s, when an unknown printer took a galley of type and scrambled it to make a type specimen book. It has survived not only five centuries,</p>
  </article>
  <article class="abs news-item" style="top:232px">
    <div class="photo" role="img" aria-label="Photo of a diver with yellow fins in deep blue water" style="background:linear-gradient(160deg,#0d5aa0,#2287cc)"></div>
    <div class="news-head">Nemo Enim Ipsam Volup</div>
    <div class="news-date">09-07-2015</div>
    <p class="news-text">Lorem Ipsum has been the industry's standard dummy text ever since the 1500s, when an unknown printer took a galley of type and scrambled it to make a type specimen book. It has survived not only five centuries,</p>
  </article>

  <form class="abs search-panel">
    <div class="search-title">SEARCH FOR YOUR DREAM<br>CHARTER TODAY!</div>
    <div class="radio" style="top:82px"><i></i>I have approximate dates</div>
    <div class="radio" style="top:105px"><i></i>I'm flexible</div>
    <div class="field" style="top:139px">First Name</div>
    <div class="field" style="top:199px">Email</div>
    <div class="btn-find">FIND CHARTERS</div>
  </form>
</section>

<footer class="abs site-footer">
  <div class="foot-title" style="left:89px">LINKS</div>
  <ul class="foot-links">
    <li>Customer Support</li><li>Documentation</li><li>Resources</li><li>General FAQs</li><li>Shortcodes</li>
  </ul>
  <div class="foot-title" style="left:298px">SCHEDULE</div>
  <div class="foot-text" style="left:298px;top:75px;width:235px">&nbsp;Lorem Ipsum has been the industry's standard dummy text ever since the 1500s, when an unknown printer took</div>
  <div class="foot-text" style="left:298px;top:134px;width:235px">a galley of type and scrambled it to make a type specimen book. It has survived not only five centuries, but also the leap into electronic</div>
  <div class="foot-title" style="left:649px">GET IN TOUCH</div>
  <div class="foot-text" style="left:649px;top:75px;width:200px;line-height:26px">Address : 12 Coral Reef Avenue, Harbor Bay 6100, St. Thomas<br>Phone : (08) 95550100<br>Email : info@tealfathom.com</div>
  <div class="foot-title" style="left:905px">NEWSLETTER</div>
  <div class="foot-text" style="left:905px;top:75px;width:210px">Your about us information would fit here nicely.</div>
  <div class="newsletter-form"><div class="email">Email address</div><div class="submit">Submit</div></div>
  <div class="foot-icons"><span></span><span></span><span></span></div>
</footer>

<div class="abs copyright">Copyright © 2016. All Rights Reserved</div>

</body>
</html>
```